Copper Ridge Jerky packaging

We are looking for a modern, upmarket packaging for our range of beef jerky. Our existing logo is attached for your reference.
We aim to have our product placed in gastro pubs, craft beer events, bottle shops and hotels. The retail package itself will be 60g net and approximately 17cm x 14cm. There will be 4 flavours (original, chilli, smoked pepper and mongolian).
We would like to see some illustration in the design to showcase the different flavours. Use of colour and/or window is optional.

```html
<!DOCTYPE html>
<html lang="en">
<head>
<meta charset="utf-8">
<title>Copper Ridge Jerky – Beef Jerky Original</title>
<link rel="stylesheet" href="https://fonts.googleapis.com/css2?family=Bebas+Neue&family=Oswald:wght@400;500&family=Dancing+Script:wght@700&display=swap">
<style>
  :root {
    --backdrop: #e4e4e4;
    --pouch-red: #9b1a24;
    --pouch-red-dark: #7a121b;
    --pouch-black: #0d0d0d;
    --ink-white: #f1f1f1;
    --accent-red: #d4202c;
    --meat-light: #a8402e;
    --meat-dark: #3d130c;
  }
  * { margin: 0; padding: 0; box-sizing: border-box; }
  html, body { width: 1200px; height: 900px; overflow: hidden; }
  body {
    background: var(--backdrop);
    display: flex; align-items: center; justify-content: center;
    font-family: "Oswald", sans-serif;
  }
  .pouch {
    position: relative;
    width: 452px; height: 580px;
    background: var(--pouch-red);
    border-radius: 4px;
    overflow: hidden;
  }
  .pouch__seal {
    position: absolute; left: 0; right: 0; top: 0; height: 26px;
    background: repeating-linear-gradient(to bottom, var(--pouch-red) 0 3px, var(--pouch-red-dark) 3px 5px);
  }
  .pouch__panel {
    position: absolute; left: 0; right: 0; top: 28px; bottom: 48px;
    background: var(--pouch-black);
    clip-path: polygon(50% 0, 100% 84px, 100% 100%, 0 100%, 0 84px);
  }
  .pouch__base {
    position: absolute; left: 0; right: 0; bottom: 0; height: 48px;
    background: var(--pouch-red);
  }
  .brand {
    position: absolute; top: 96px; left: 0; right: 0;
    text-align: center; color: var(--ink-white);
    font-weight: 500; font-size: 30px; line-height: 1.05; letter-spacing: 3px;
    text-transform: uppercase;
  }
  .product-name {
    position: absolute; top: 196px; left: 0; right: 0;
    text-align: center; color: var(--ink-white);
    font-family: "Bebas Neue", sans-serif; font-size: 86px; line-height: 1;
    letter-spacing: 1px;
  }
  .flavour {
    position: absolute; top: 284px; left: 0; right: 0;
    display: flex; align-items: center; justify-content: center; gap: 12px;
  }
  .flavour__name {
    font-family: "Dancing Script", cursive; color: var(--accent-red);
    font-size: 38px; line-height: 1;
  }
  .flavour__rule { width: 80px; height: 10px; }
  .claim {
    position: absolute; top: 334px; left: 0; right: 0;
    text-align: center; color: var(--ink-white);
    font-size: 20px; letter-spacing: -0.3px; text-transform: uppercase;
  }
  .claim__highlight { color: var(--accent-red); }
  .hero-image {
    position: absolute; left: 40px; right: 76px; top: 370px; height: 100px;
    background: linear-gradient(90deg, var(--meat-light) 0%, #6e2417 35%, var(--meat-dark) 70%, #4a1a12 100%);
  }
  .origin {
    position: absolute; top: 478px; left: 0; right: 0;
    text-align: center; color: var(--ink-white);
    font-size: 20px; letter-spacing: -0.3px; text-transform: uppercase;
  }
  .net-weight {
    position: absolute; left: 196px; bottom: 22px; width: 66px; height: 50px;
    background: var(--pouch-black);
    border-left: 1px solid var(--accent-red); border-right: 1px solid var(--accent-red);
    display: flex; align-items: center; justify-content: center;
    color: var(--ink-white); font-size: 30px; line-height: 1;
  }
</style>
</head>
<body>
  <div class="pouch">
    <div class="pouch__seal"></div>
    <div class="pouch__panel"></div>
    <div class="pouch__base"></div>

    <div class="brand">Copper Ridge<br>Jerky</div>

    <h1 class="product-name">Beef Jerky</h1>

    <div class="flavour">
      <svg class="flavour__rule" viewBox="0 0 80 10" aria-hidden="true">
        <line x1="2" y1="5" x2="78" y2="5" stroke="#f1f1f1" stroke-width="1.5"/>
        <polygon points="0,5 6,2 6,8" fill="#f1f1f1"/>
        <polygon points="66,1 78,5 66,9" fill="#f1f1f1"/>
      </svg>
      <span class="flavour__name">Original</span>
      <svg class="flavour__rule" viewBox="0 0 80 10" aria-hidden="true">
        <line x1="2" y1="5" x2="78" y2="5" stroke="#f1f1f1" stroke-width="1.5"/>
        <polygon points="2,1 14,5 2,9" fill="#f1f1f1"/>
        <polygon points="80,5 74,2 74,8" fill="#f1f1f1"/>
      </svg>
    </div>

    <p class="claim">Made with <span class="claim__highlight">100%</span> grass-fed beef</p>

    <div class="hero-image" role="img" aria-label="Raw steak with garlic and peppercorns beside strips of dried beef jerky"></div>

    <p class="origin">Made in Australia</p>

    <div class="net-weight">60gr</div>
  </div>
</body>
</html>
```